Brannowick Ltd
Marketting material for Construction Company - Construction
Marketting material for Construction Company
Construction
All types of householders
Brochure is to be delivered through the doors of targeted areas in London. It should be clear, modern and colourful in design.
Concepts
Rack Card for Contractor Network
tolvimar tolvimar
please see the revised text in the download section. Spelling mistakes have been corrected and a Design and Build section has been added
Contact information for brochure. tel: 02079314827 Address: 14-16 Marrowby Street London N4 2PX. Name: Mavin Tollers Company: Brannowick ltd

```html
<!DOCTYPE html>
<html lang="en">
<head>
<meta charset="utf-8">
<title>Brannowick Ltd – Brochure</title>
<link href="https://fonts.googleapis.com/css2?family=Montserrat:wght@600;700;800&family=Open+Sans:wght@400;600&display=swap" rel="stylesheet">
<style>
:root{
  --bg:#d6d6d6;
  --navy:#262a6e;
  --red:#c8202b;
  --red-dark:#a3161f;
  --white:#ffffff;
  --ink:#3a3a3a;
  --room-light:#ece9e4;
  --room-mid:#b9b2a8;
  --floor:#5a4434;
}
*{margin:0;padding:0;box-sizing:border-box}
html,body{width:1200px;height:859px;overflow:hidden;background:var(--bg)}
body{position:relative;font-family:"Open Sans",Arial,sans-serif;color:var(--ink)}
.spread{position:absolute;top:231px;width:560px;height:396px;background:var(--white);box-shadow:0 6px 18px rgba(0,0,0,.25)}
.cover-spread{left:20px}
.inside-spread{left:620px}
.panel{position:absolute;top:0;width:280px;height:396px;overflow:hidden}
.panel-back{left:0}
.panel-front{left:280px}
.panel svg,.inside-spread svg.layer{position:absolute;inset:0}
.philosophy{position:absolute;left:16px;top:22px;width:200px;color:var(--white)}
.philosophy h2{font-family:"Montserrat",Arial,sans-serif;font-size:9px;font-weight:800;text-transform:uppercase;margin-bottom:6px;letter-spacing:.5px}
.philosophy p{font-size:7px;line-height:1.45}
.cover-question{position:absolute;left:0;top:14px;width:280px;text-align:center;color:var(--white);font-family:"Montserrat",Arial,sans-serif;font-weight:700;font-size:9.5px;line-height:1.35}
.brand{position:absolute;left:0;top:322px;width:280px;display:flex;justify-content:center;align-items:center;gap:8px}
.brand-mark{width:14px;height:14px;background:var(--red)}
.brand-name{font-family:"Montserrat",Arial,sans-serif;font-weight:700;font-size:28px;color:var(--red-dark);letter-spacing:.5px}
.service{position:absolute;width:150px}
.service h3{display:inline-block;background:var(--red);color:var(--white);font-family:"Montserrat",Arial,sans-serif;font-weight:700;font-size:7.5px;text-transform:uppercase;padding:3px 8px;margin-bottom:5px}
.service p{font-size:6.5px;line-height:1.5}
.service-right{text-align:right}
.contact-band{position:absolute;left:0;bottom:0;width:560px;height:26px;background:var(--red);color:var(--white);display:flex;justify-content:center;align-items:center;gap:24px;font-family:"Montserrat",Arial,sans-serif;font-weight:600;font-size:7.5px}
</style>
</head>
<body>

<section class="spread cover-spread">
  <div class="panel panel-back">
    <svg width="280" height="396" viewBox="0 0 280 396">
      <defs>
        <linearGradient id="roomBack" x1="0" y1="0" x2="0" y2="1">
          <stop offset="0" stop-color="var(--room-light)"/>
          <stop offset=".6" stop-color="var(--room-mid)"/>
          <stop offset="1" stop-color="var(--floor)"/>
        </linearGradient>
      </defs>
      <polygon points="0,0 280,0 280,160 0,232" fill="var(--red)"/>
      <polygon points="0,232 280,160 280,176 0,248" fill="var(--white)"/>
      <polygon points="0,248 280,176 280,186 0,258" fill="var(--navy)"/>
      <polygon role="img" aria-label="Photo of a bright empty room with a dark wooden floor" points="0,258 280,186 280,396 0,396" fill="url(#roomBack)"/>
    </svg>
    <div class="philosophy">
      <h2>Our Philosophy</h2>
      <p>Brannowick ltd is a family run building firm serving homes across London. We take pride in quality work, clear prices and tidy sites. Every project is managed from first visit to final finish by our own experienced team.</p>
    </div>
  </div>

  <div class="panel panel-front">
    <svg width="280" height="396" viewBox="0 0 280 396">
      <defs>
        <linearGradient id="roomFront" x1="0" y1="0" x2="0" y2="1">
          <stop offset="0" stop-color="#f4f2ee"/>
          <stop offset=".55" stop-color="#d8d2ca"/>
          <stop offset="1" stop-color="var(--floor)"/>
        </linearGradient>
      </defs>
      <rect x="0" y="0" width="280" height="110" fill="var(--navy)"/>
      <polygon role="img" aria-label="Photo of a spacious open room with tall windows and a wooden floor" points="0,150 140,84 280,150 280,300 0,300" fill="url(#roomFront)"/>
      <polyline points="0,150 140,84 280,150" fill="none" stroke="var(--red)" stroke-width="7"/>
    </svg>
    <p class="cover-question">Are you looking for a larger kitchen?<br>A new bathroom? Or<br>want to add an extension to your home?<br>Perhaps a loft conversion is the way to go!</p>
    <div class="brand">
      <span class="brand-mark"></span>
      <span class="brand-name">Brannowick</span>
    </div>
  </div>
</section>

<section class="spread inside-spread">
  <svg class="layer" width="560" height="396" viewBox="0 0 560 396">
    <defs>
      <linearGradient id="roomWide" x1="0" y1="0" x2="0" y2="1">
        <stop offset="0" stop-color="#e9e6e1"/>
        <stop offset=".5" stop-color="#9a9088"/>
        <stop offset="1" stop-color="#6b5444"/>
      </linearGradient>
      <linearGradient id="roomSmall" x1="0" y1="0" x2="0" y2="1">
        <stop offset="0" stop-color="#ddd6cc"/>
        <stop offset="1" stop-color="#7a6050"/>
      </linearGradient>
    </defs>
    <path role="img" aria-label="Photo of an open plan kitchen extension with folding glass doors" d="M0,10 Q280,-6 560,10 L560,170 Q280,150 0,170 Z" fill="url(#roomWide)"/>
    <path d="M0,170 Q280,150 560,170" fill="none" stroke="var(--red)" stroke-width="4"/>
    <rect role="img" aria-label="Photo of a finished living room" x="178" y="180" width="204" height="84" fill="url(#roomSmall)"/>
    <rect role="img" aria-label="Photo of a loft staircase" x="178" y="270" width="99" height="88" fill="url(#roomSmall)"/>
    <rect role="img" aria-label="Photo of a new kitchen" x="283" y="270" width="99" height="88" fill="url(#roomSmall)"/>
  </svg>

  <div class="service" style="left:14px;top:192px">
    <h3>Extensions</h3>
    <p>We design and build single and double storey extensions that add light and space.</p>
  </div>
  <div class="service" style="left:14px;top:272px">
    <h3>Loft Conversions</h3>
    <p>Turn unused roof space into a bedroom, office or bathroom with full approvals.</p>
  </div>
  <div class="service service-right" style="left:396px;top:192px">
    <h3>Kitchens</h3>
    <p>Bespoke kitchens fitted by our own trades, from first plan to final tile.</p>
  </div>
  <div class="service service-right" style="left:396px;top:272px">
    <h3>Design &amp; Build</h3>
    <p>One team handles drawings, planning and building so your project runs smoothly.</p>
  </div>

  <div class="contact-band">
    <span>Mavin Tollers</span>
    <span>tel: 02079460318</span>
    <span>14-16 Marrowby Street London N4 2PX</span>
  </div>
</section>

</body>
</html>
```